Fahrzeugbeschriftung für Vorma Tilesko 2012 Kasten
Zielgruppe
Werbetechnik aller Art, siehe www.belmento.de
Aufgabenstellung
Es wird ein pfiffiges Design gesucht. Eine Vollverklebung ist nicht möglich, größere Flächen allerdings schon. Gerne auch mit Werbegesicht, also nicht so langweilig wie die bisherige Beklebung.
www.belmento.de

```html
<!DOCTYPE html>
<html lang="de">
<head>
<meta charset="utf-8">
<title>Belmento Werbezentrum – Fahrzeugbeschriftung</title>
<link rel="stylesheet" href="https://fonts.googleapis.com/css2?family=Roboto+Condensed:wght@400;700&display=swap">
<style>
  :root {
    --bg: #8c8c8c;
    --body: #ffffff;
    --orange: #e8791c;
    --grey: #5f5d5e;
    --dark: #2b2b2b;
    --tyre: #1e1e1e;
    --rim: #b9b9b9;
    --glass: #3a3f44;
    --photo-a: #c9a27e;
    --photo-b: #7a5537;
  }
  html, body {
    margin: 0;
    width: 1200px;
    height: 506px;
    overflow: hidden;
    background: var(--bg);
  }
  .livery {
    display: block;
    width: 1200px;
    height: 506px;
    font-family: "Roboto Condensed", "Arial Narrow", sans-serif;
  }
  .van-body { fill: var(--body); }
  .skirt { fill: var(--tyre); }
  .window { fill: var(--glass); }
  .orange { fill: var(--orange); }
  .grey { fill: var(--grey); }
  .tyre { fill: var(--tyre); }
  .rim { fill: var(--rim); }
  .brand-name { fill: var(--dark); font-weight: 700; }
  .brand-sub { fill: var(--orange); font-weight: 400; letter-spacing: 1px; }
  .services { fill: var(--dark); font-weight: 700; font-size: 16px; }
  .tick { fill: none; stroke: var(--orange); stroke-width: 3; stroke-linecap: round; stroke-linejoin: round; }
  .slogan { fill: var(--orange); font-weight: 700; font-size: 17.5px; }
  .web { fill: #fff; font-weight: 700; font-size: 27px; }
  .phone { fill: #fff; font-weight: 700; font-size: 21px; }
  .address-strip { fill: var(--dark); }
  .address { fill: #fff; font-weight: 700; font-size: 13px; }
</style>
</head>
<body>
<svg class="livery" viewBox="0 0 1200 506" xmlns="http://www.w3.org/2000/svg">
  <defs>
    <linearGradient id="photoTone" x1="0" y1="0" x2="0" y2="1">
      <stop offset="0" stop-color="var(--photo-a)"/>
      <stop offset="1" stop-color="var(--photo-b)"/>
    </linearGradient>
    <clipPath id="bodyClip">
      <path d="M124 395 L124 268 Q130 238 160 228 L270 118 Q300 82 360 70 L1030 62 Q1062 64 1066 100 L1070 360 Q1068 392 1040 396 Z"/>
    </clipPath>
  </defs>

  <g class="vehicle">
    <path class="van-body" d="M124 395 L124 268 Q130 238 160 228 L270 118 Q300 82 360 70 L1030 62 Q1062 64 1066 100 L1070 360 Q1068 392 1040 396 Z"/>

    <g class="graphics" clip-path="url(#bodyClip)">
      <path class="orange" d="M120 400 L310 60 L370 60 L180 400 Z"/>
      <path class="grey" d="M340 400 L540 60 L560 60 L360 400 Z"/>
      <path class="orange" d="M380 400 L580 60 L790 60 Q770 200 865 400 Z"/>
      <path class="grey" d="M800 60 L820 60 Q790 220 880 400 L860 400 Q770 220 800 60 Z"/>
    </g>

    <path class="window" d="M290 110 Q320 84 370 80 L460 78 L460 180 L255 185 Z"/>
    <path class="skirt" d="M124 360 L1070 360 L1068 400 L124 400 Z"/>
    <circle class="tyre" cx="255" cy="400" r="58"/>
    <circle class="rim" cx="255" cy="400" r="34"/>
    <circle class="tyre" cx="915" cy="400" r="58"/>
    <circle class="rim" cx="915" cy="400" r="34"/>
  </g>

  <rect class="photo" x="568" y="52" width="196" height="224" rx="80" fill="url(#photoTone)" role="img" aria-label="Werbegesicht: Frau kopfüber, die Hände an den Wangen, mit erstauntem Ausdruck"/>

  <g class="brand brand-front">
    <text class="brand-name" x="262" y="272" font-size="30">Belmento</text>
    <text class="brand-sub" x="264" y="288" font-size="9">WERBEZENTRUM</text>
  </g>

  <g class="brand brand-main">
    <text class="brand-name" x="843" y="108" font-size="58">Belmento</text>
    <text class="brand-sub" x="906" y="130" font-size="16">WERBEZENTRUM</text>
  </g>

  <g class="service-list">
    <path class="tick" d="M864 178 L869 184 L878 172"/>
    <text class="services" x="884" y="186">DIGITALE MEDIEN</text>
    <path class="tick" d="M864 200 L869 206 L878 194"/>
    <text class="services" x="884" y="208">DRUCK + VEREDELUNG</text>
    <path class="tick" d="M864 222 L869 228 L878 216"/>
    <text class="services" x="884" y="230">WERBETECHNIK</text>
  </g>

  <g class="claim">
    <text class="slogan" x="883" y="260">Werbung kann jeder,</text>
    <text class="slogan" x="883" y="282">aber wir können es</text>
    <text class="slogan" x="883" y="304">einfach besser!</text>
  </g>

  <g class="contact">
    <text class="web" x="550" y="304">www.belmento.de</text>
    <text class="phone" x="536" y="330">Phone 07000-482913-0</text>
    <rect class="address-strip" x="382" y="343" width="400" height="25" rx="3"/>
    <text class="address" x="516" y="361">Lindenweg 14, 70000 musterstadt</text>
  </g>
</svg>
</body>
</html>
```